A welcome booklet to put in our guest bags for our church visitos to look at

We would like a booklet for our guest to have that gives an over all of our church and shows us to be friendly -0 enough information but not too much reading - good logo's and graphics

Target Market(s)

20’s - 30’s

Font styles to use
Serif
Sans Serif

Colors

Designer to choose colors to be used in the design.

Requirements
Must have
• It must have our logo and the church information and please stick to the wording in the booklet ... fresh pictures of people
Nice to have
• It has to look contemporary and fresh
Should not have
• Old fashioned and typically churchy - no religious symbols or Uber Christian type appearance

```html
<!DOCTYPE html>
<html lang="en">
<head>
<meta charset="utf-8">
<title>Harbourgate City Church – Welcome Booklet Spread</title>
<link rel="stylesheet" href="https://fonts.googleapis.com/css2?family=Exo+2:ital,wght@0,300;0,600;0,800;1,300;1,800&family=Open+Sans:wght@400;600;700&display=swap">
<style>
  :root {
    --bg: #e9eef0;
    --paper: #ffffff;
    --ink: #3d3d3d;
    --blue: #1f86b8;
    --blue-deep: #1a6f9c;
    --teal: #33b5a8;
    --teal-light: #3fbdb8;
    --green: #8cc04d;
    --orange: #f29a2e;
    --magenta: #b8328a;
    --yellow: #d8d33a;
    --photo-light: #e3e23a;
    --photo-dark: #2b2d16;
  }
  * { box-sizing: border-box; margin: 0; padding: 0; }
  html, body { width: 1200px; height: 833px; overflow: hidden; background: var(--bg); }
  body { font-family: "Open Sans", Arial, sans-serif; color: var(--ink); }

  .spread {
    position: absolute; left: 60px; top: 34px;
    width: 1080px; height: 764px;
    display: flex;
    box-shadow: 0 6px 24px rgba(0,0,0,.15);
  }
  .page { position: relative; width: 540px; height: 764px; background: var(--paper); overflow: hidden; }
  .page--left { border-right: 1px solid #e2e2e2; }

  .brand {
    position: absolute; top: 30px; right: 34px;
    font-family: "Exo 2", sans-serif; font-weight: 800; font-size: 13px;
    color: #222; display: flex; align-items: center; gap: 6px; width: 110px; line-height: 1.05;
  }
  .brand__square { width: 12px; height: 12px; background: #222; flex: none; }

  .page-title {
    position: absolute; left: 44px; top: 44px;
    font-family: "Exo 2", sans-serif; font-size: 27px; color: var(--blue);
    font-style: italic; font-weight: 800; letter-spacing: .5px;
  }
  .page-title span, .section-title span { font-weight: 300; font-style: normal; color: var(--teal-light); }

  .cycle { position: absolute; left: 60px; top: 90px; }
  .cycle text { font-family: "Exo 2", sans-serif; font-weight: 800; font-size: 12px; }

  .section-title {
    position: absolute; left: 44px;
    font-family: "Exo 2", sans-serif; font-size: 18px; color: var(--blue);
    font-style: italic; font-weight: 800;
  }
  .copy { position: absolute; font-size: 9px; line-height: 1.5; color: #555; }
  .copy p + p { margin-top: 6px; }

  .contacts { position: absolute; list-style: none; font-size: 10px; color: #333; }
  .contacts li { display: flex; align-items: center; gap: 12px; height: 24px; }
  .dot {
    width: 20px; height: 20px; border-radius: 50%; flex: none;
    display: flex; align-items: center; justify-content: center;
  }
  .dot--grey { background: #555; } .dot--blue { background: var(--blue); }
  .dot--green { background: var(--green); } .dot--red { background: #d8343a; }
  .dot--navy { background: #2f4f98; } .dot--sky { background: #2ea3dc; }

  .colour-strip { position: absolute; bottom: 62px; left: 0; display: flex; gap: 6px; }
  .colour-strip i { display: block; width: 66px; height: 10px; }
  .colour-strip i:nth-child(1) { background: var(--yellow); }
  .colour-strip i:nth-child(2) { background: var(--teal); }
  .colour-strip i:nth-child(3) { background: var(--magenta); }
  .colour-strip i:nth-child(4) { background: var(--green); }
  .colour-strip i:nth-child(5) { background: var(--blue); }
  .folio-rule { position: absolute; bottom: 40px; height: 1px; background: var(--blue); }
  .folio {
    position: absolute; bottom: 30px; font-family: "Exo 2", sans-serif;
    font-weight: 600; font-size: 14px; color: var(--magenta);
    border-left: 1px solid var(--blue); border-right: 1px solid var(--blue); padding: 0 6px;
  }

  .banner {
    position: absolute; left: 0; right: 0; top: 100px; height: 210px;
    background: radial-gradient(ellipse at 55% 20%, var(--photo-light) 0%, #b9b92c 35%, #6b6b22 65%, var(--photo-dark) 100%);
  }
  .banner-band {
    position: absolute; left: 60px; top: 70px; width: 92px; height: 260px;
    background: rgba(31,134,184,.82);
  }
  .headline {
    position: absolute; left: 60px; top: 148px;
    font-family: "Exo 2", sans-serif; font-weight: 800; color: #fff; line-height: 1;
  }
  .headline__small { font-size: 18px; display: block; }
  .headline__big { font-size: 38px; display: block; }
  .headline__accent { color: var(--teal-light); font-size: 22px; }

  .life-bar { position: absolute; left: 60px; top: 560px; width: 14px; height: 110px; background: var(--blue); }
  .life-mark {
    position: absolute; left: 100px; top: 594px;
    font-family: "Exo 2", sans-serif; font-weight: 800; font-size: 30px; color: var(--blue-deep);
  }
  .link { color: var(--blue); font-weight: 700; }
</style>
</head>
<body>
<main class="spread">

  <section class="page page--left">
    <div class="brand"><span class="brand__square"></span>Harbourgate City Church</div>
    <h1 class="page-title">DISCIPLESHIP <span>AT HCC</span></h1>

    <svg class="cycle" width="340" height="230" viewBox="0 0 340 230" aria-label="Discipleship cycle: connect, come, serve, grow">
      <g stroke="#999" stroke-dasharray="3 3" stroke-width="1">
        <line x1="170" y1="118" x2="95" y2="42"/><line x1="170" y1="118" x2="265" y2="70"/>
        <line x1="170" y1="118" x2="60" y2="170"/><line x1="170" y1="118" x2="240" y2="200"/>
      </g>
      <circle cx="170" cy="118" r="46" fill="#b8328a"/>
      <circle cx="170" cy="118" r="52" fill="none" stroke="#555" stroke-width="1.2"/>
      <text x="170" y="114" text-anchor="middle" fill="#fff" font-size="11">Harbourgate</text>
      <text x="170" y="128" text-anchor="middle" fill="#fff" font-size="11">City Church</text>
      <circle cx="95" cy="42" r="20" fill="#f29a2e"/><circle cx="95" cy="42" r="24" fill="none" stroke="#f29a2e"/>
      <text x="95" y="80" text-anchor="middle" fill="#f29a2e">CONNECT</text>
      <circle cx="265" cy="70" r="20" fill="#8cc04d"/><circle cx="265" cy="70" r="24" fill="none" stroke="#8cc04d"/>
      <text x="290" y="110" text-anchor="middle" fill="#8cc04d">COME</text>
      <circle cx="60" cy="170" r="20" fill="#1f86b8"/><circle cx="60" cy="170" r="24" fill="none" stroke="#1f86b8"/>
      <text x="60" y="134" text-anchor="middle" fill="#1f86b8">GROW</text>
      <circle cx="240" cy="200" r="20" fill="#33b5a8"/><circle cx="240" cy="200" r="24" fill="none" stroke="#33b5a8"/>
      <text x="262" y="165" text-anchor="middle" fill="#33b5a8">SERVE</text>
    </svg>

    <h2 class="section-title" style="top:336px">GET <span>CONNECTED</span></h2>
    <div class="copy" style="left:44px; top:366px; width:440px">
      <p>We need relationships to grow and we would love you stay in touch with you. Please fill out our connect card that is in this pack. HCC complies with the General Data Protection Regulation (GDPR).</p>
      <p>Additionally, there are a number of ways that you can contact us. Please let us know how you found your first time at HCC; we would love to hear from you and are looking forward to getting to know you.</p>
    </div>

    <h2 class="section-title" style="top:456px">FILL IN A <span>CONNECT CARD</span></h2>
    <ul class="contacts" style="left:44px; top:494px">
      <li><span class="dot dot--grey"><svg width="10" height="10" viewBox="0 0 10 10"><path d="M2 1l2 2-1 1.3c.6 1.2 1.5 2.1 2.7 2.7L7 6l2 2-1.3 1.3C4.5 9 1 5.5.7 2.3z" fill="#fff"/></svg></span>Call us on :- 0100 555 0142</li>
      <li><span class="dot dot--blue"><svg width="11" height="8" viewBox="0 0 11 8"><rect x=".5" y=".5" width="10" height="7" fill="none" stroke="#fff"/><path d="M.5.5l5 4 5-4" fill="none" stroke="#fff"/></svg></span>Email us @ admin@hcc.community</li>
      <li><span class="dot dot--green"><svg width="10" height="10" viewBox="0 0 10 10"><circle cx="5" cy="5" r="4.3" fill="none" stroke="#fff"/><path d="M.7 5h8.6M5 .7v8.6" stroke="#fff"/></svg></span>Check us out @ www.hcc.community</li>
    </ul>
    <ul class="contacts" style="left:270px; top:494px">
      <li><span class="dot dot--red"></span>Video channel @ Harbourgate City Church</li>
      <li><span class="dot dot--navy"></span>Community page @ Harbourgate City Church</li>
      <li><span class="dot dot--sky"></span>Short posts @ hcc_news</li>
    </ul>

    <div class="colour-strip"><i></i><i></i><i></i><i></i><i></i></div>
    <div class="folio-rule" style="left:0; width:430px"></div>
    <div class="folio" style="left:440px">3</div>
  </section>

  <section class="page page--right">
    <div class="brand" style="top:30px"><span class="brand__square"></span>Harbourgate City Church</div>
    <div class="banner" role="img" aria-label="Photo of a person leaping on a hilltop against a bright yellow sky"></div>
    <div class="banner-band"></div>
    <h2 class="headline">
      <span class="headline__small">JOIN A</span>
      <span class="headline__big">LIFE GROUP OR</span>
      <span class="headline__small">ATTEND <span class="headline__accent">ONE OF OUR COURSE</span></span>
    </h2>

    <div class="copy" style="left:60px; top:350px; width:420px">
      <p>Our various Life Groups are located in different parts of the city and they meet every fortnight or once a month. We run various courses in the year that will set you on a journey to discover faith and help you live in the will of God. There will be something that you will find enriching. As you connect to a group or attend a course you will find enriching teaching but also build great friendships and grow as a person.</p>
      <p>For our new members, a great start would be for you to attend HCC Life course. We would love to get to know you and help you settle into the HCC family. If you would to join a Life Group, please come along to our Central Life Group which takes place here at the church on <span class="link">Wednesdays</span> from <span class="link">7:30- 9:00pm.</span></p>
      <p>To find out more about our Life Groups, please visit:- <span class="link">www.hcc.community/life-groups</span> and for more information about our courses, please visit <span class="link">www.hcc.community/courses</span></p>
    </div>

    <div class="life-bar"></div>
    <div class="life-mark">Life Groups at HCC</div>

    <div class="colour-strip"><i></i><i></i><i></i><i></i><i></i></div>
    <div class="folio-rule" style="left:0; width:480px"></div>
    <div class="folio" style="left:488px">4</div>
  </section>

</main>
</body>
</html>
```